Webdesign für Selbsthilfegruppe für Gehörlose
Zielgruppe
(Un)gesehene Schwestern Chemnitz und Umgebung ist eine Selbsthilfegruppe
Wir sind eine Gruppe von Frauen mit und ohne Hörschädigungen sowie Traumaerfahrungen.
Die SHG berät allen Arten der Hörschädigung und Traumafolgen von betroffene Frauen.
Schwerpunkte der Arbeit:
Zurück in das ICH finden mit Unterstützung, Aufklärung, Erkennen, Benennen, Handlen und Vermittlung von Behandlungen sowie Rehabilitation und Rückfallprävention
Weiteres entnehmen Sie bitte aus dem Flyer
Aufgabenstellung
Barrierefreiheit der Website für Menschen mit Hörbehinderung

```html
<!DOCTYPE html>
<html lang="de">
<head>
<meta charset="utf-8">
<title>SHG (Un)gesehene Schwestern</title>
<link href="https://fonts.googleapis.com/css2?family=Open+Sans:wght@400;600;700&display=swap" rel="stylesheet">
<style>
:root{
  --berry:#a13d6e;
  --blush:#f9e3e6;
  --blush-soft:#fcefef;
  --field:#fbe6e8;
  --text:#4a4a4a;
  --muted:#6b6b6b;
  --white:#ffffff;
}
*{box-sizing:border-box;margin:0;padding:0}
html,body{width:1200px;height:3829px;overflow:hidden}
body{position:relative;font-family:"Open Sans",sans-serif;color:var(--text);background:var(--white);font-size:13px;line-height:20px}
.abs{position:absolute}
.site-header{left:0;top:0;width:1200px;height:78px;background:var(--berry)}
.brand{left:89px;top:6px;width:64px;height:64px;border-radius:50%;background:var(--white);display:flex;align-items:center;justify-content:center;text-align:center;font-size:8px;line-height:10px;font-weight:600;color:var(--berry);padding:6px}
.nav-main{left:262px;top:44px;display:flex;font-size:13.5px;color:var(--white)}
.nav-main a{color:var(--white);text-decoration:none;margin-right:40px}
.nav-meta{left:965px;top:10px;display:flex;gap:20px;font-size:12px;color:var(--white);align-items:center}
.nav-meta span{display:flex;align-items:center;gap:6px}
.hero{left:0;top:78px;width:1200px;height:468px;background:var(--blush)}
.hero-title{left:174px;top:324px;font-size:30px;line-height:42px;font-weight:700;color:var(--berry)}
.hero-emblem{left:571px;top:140px;width:300px;height:300px;border-radius:50%;border:2px solid var(--berry);display:flex;align-items:center;justify-content:center;text-align:center;font-size:20px;line-height:28px;font-weight:600;color:var(--berry);padding:40px}
.deco{border-radius:50%}
.band-white{left:0;top:546px;width:1200px;height:465px;background:linear-gradient(90deg,#fff 40%,#fdf0f1)}
.band-pink{left:0;width:1200px;background:var(--blush-soft)}
.photo-ring{border-radius:50%;background:#fbe5e8}
.photo{border-radius:50%}
.heading{font-size:19px;line-height:24px;font-weight:700;color:var(--berry)}
.heading-bar{width:36px;height:4px;background:var(--berry)}
.copy{font-size:13px;line-height:20px;color:var(--text)}
.btn{height:30px;border-radius:15px;background:var(--berry);color:var(--white);font-size:13.5px;display:flex;align-items:center;justify-content:center}
.focus-icon{width:98px;height:98px;border-radius:50%;background:var(--berry);display:flex;align-items:center;justify-content:center}
.focus-label{width:160px;text-align:center;font-size:13.5px;color:var(--muted)}
.news-card{width:248px}
.news-img{width:248px;height:147px;border-radius:6px}
.news-title{font-size:13px;line-height:20px;font-weight:700;color:var(--berry);margin-top:24px}
.news-text{font-size:13px;line-height:20px;color:var(--text);margin-top:20px}
.news-card .btn{width:121px;margin-top:22px}
.field{background:var(--field);font-size:13px;color:var(--muted);padding:15px 14px}
.check{width:18px;height:18px;background:var(--field)}
.site-footer{left:0;top:3579px;width:1200px;height:186px;background:var(--berry);color:var(--white)}
.foot-col{top:58px;display:flex;gap:14px;font-size:13.5px;line-height:20px}
.foot-div{top:30px;width:2px;height:128px;background:var(--white)}
.to-top{left:1128px;top:3688px;width:48px;height:48px;border-radius:50%;background:var(--white);color:var(--berry);font-size:10px;display:flex;flex-direction:column;align-items:center;justify-content:center;line-height:10px}
.legal{left:0;top:3765px;width:1200px;height:64px;font-size:13.5px;color:var(--text)}
.legal a{color:var(--text);text-decoration:none}
</style>
</head>
<body>

<header class="abs site-header">
  <div class="abs brand">(Un)gesehene Schwestern</div>
  <nav class="abs nav-main"><a>Home</a><a>Über Uns</a><a>Das Team</a><a>Das Trauma</a><a>Hörschädigung</a><a>Aktuelles</a><a>Netzwerkpartner</a></nav>
  <div class="abs nav-meta">
    <span><svg width="20" height="16" viewBox="0 0 20 16" fill="none" stroke="#fff" stroke-width="1.3"><rect x="1" y="1" width="13" height="9" rx="1"/><path d="M6 10v4l3-4M16 5h3v8h-2v2l-2-2h-5"/></svg>Kontakt</span>
    <span>Förderer</span>
  </div>
</header>

<section class="abs hero">
  <div class="abs deco" role="img" aria-label="Aquarellierte Blätter und Blüte" style="left:0;top:0;width:360px;height:200px;background:radial-gradient(ellipse at 40% 50%,#e9d3cd 0%,rgba(249,227,230,0) 70%)"></div>
  <div class="abs deco" role="img" aria-label="Aquarellierte Blätter und rosa Blüte" style="left:820px;top:180px;width:380px;height:280px;background:radial-gradient(ellipse at 60% 50%,#d9c6c9 0%,rgba(249,227,230,0) 70%)"></div>
</section>
<h1 class="abs hero-title">Willkommen bei<br>SHG (Un)gesehene Schwestern</h1>
<div class="abs hero-emblem">SHG (Un)gesehene Schwestern Chemnitz und Umgebung</div>

<section class="abs band-white"></section>
<div class="abs photo-ring" style="left:173px;top:598px;width:326px;height:326px"></div>
<div class="abs photo" role="img" aria-label="Schwarzweißfoto einer Frau, die in Gebärdensprache spricht" style="left:192px;top:617px;width:288px;height:288px;background:linear-gradient(135deg,#bdbdbd,#5a5a5a)"></div>
<h2 class="abs heading" style="left:543px;top:657px">Wer wir sind</h2>
<div class="abs heading-bar" style="left:543px;top:691px"></div>
<div class="abs copy" style="left:543px;top:725px;width:450px">
  <p>Wir sind eine Gruppe von Frauen mit und ohne Hörschädigungen sowie Traumaerfahrungen.</p>
  <p style="margin-top:20px">Wir treffen uns in regelmässigen Abständen zu verschiedenen Aktivitäten sowie Zusammenarbeit mit Netzwerkpartnern.</p>
  <p style="margin-top:20px">Neue Mitglieder sind jederzeit herzlich willkommen!</p>
</div>
<div class="abs btn" style="left:543px;top:898px;width:132px">Mehr erfahren</div>

<section class="abs band-pink" style="top:1011px;height:372px"></section>
<div class="abs deco" role="img" aria-label="Aquarellierte rosa Blüte" style="left:0;top:1190px;width:150px;height:160px;background:radial-gradient(ellipse,#efd0cb 0%,rgba(252,239,239,0) 70%)"></div>
<h2 class="abs heading" style="left:174px;top:1057px">Unsere Schwerpunkte</h2>
<div class="abs heading-bar" style="left:174px;top:1095px"></div>
<p class="abs copy" style="left:174px;top:1125px">Zurück in das Ich finden mit Unterstützung der Netzwerkpartner bzw. Traumaverbund Mittelsachsen</p>

<div class="abs focus-icon" style="left:173px;top:1179px"><svg width="54" height="54" viewBox="0 0 54 54" fill="none" stroke="#fff" stroke-width="2" stroke-linecap="round"><circle cx="30" cy="18" r="7"/><path d="M27 25v4h6v-4M30 5v3M19 10l2 2M41 10l-2 2M16 20h3M41 20h3M6 44h12l10 4 18-9-3-3-13 5H21l5-4h10v-4H18l-12 4"/></svg></div>
<div class="abs focus-icon" style="left:326px;top:1179px"><svg width="60" height="40" viewBox="0 0 60 40" fill="none" stroke="#fff" stroke-width="2.2"><circle cx="16" cy="22" r="10"/><circle cx="44" cy="22" r="10"/><path d="M26 22c2-3 6-3 8 0M6 22l-4-4M54 22l4-4"/></svg></div>
<div class="abs focus-icon" style="left:476px;top:1179px"><svg width="54" height="54" viewBox="0 0 54 54" fill="none" stroke="#fff" stroke-width="2" stroke-linecap="round" stroke-linejoin="round"><path d="M20 12l4 14M16 26l-4-8c-1-3 3-4 4-2l6 12M24 26l-2-6c-1-3 3-4 4-1l2 6M28 24c-1-3 3-4 4-1l2 5M32 27c-1-3 3-4 4-1l3 9c2 7-3 14-12 14-6 0-9-4-12-9l-6-9c-2-3 2-5 4-3l4 5M14 6l2 3M22 3v4M29 6l-2 3"/></svg></div>
<div class="abs focus-icon" style="left:622px;top:1179px"><svg width="62" height="44" viewBox="0 0 62 44" fill="none" stroke="#fff" stroke-width="2" stroke-linecap="round" stroke-linejoin="round"><path d="M2 10l8-4 10 18-8 4zM60 10l-8-4-10 18 8 4zM18 22l8 8c2 2 4 0 3-2l4 4c2 2 4 0 3-2l2 2c2 1 4-1 2-3M44 24l-9-9-6 3c-3 1-5-1-3-3l7-6h8"/></svg></div>
<div class="abs focus-icon" style="left:776px;top:1179px"><svg width="54" height="44" viewBox="0 0 54 44" fill="none" stroke="#fff" stroke-width="2"><circle cx="27" cy="12" r="6"/><circle cx="13" cy="16" r="5"/><circle cx="41" cy="16" r="5"/><path d="M17 36v-6c0-6 5-10 10-10s10 4 10 10v6zM5 34v-4c0-5 4-7 8-7M49 34v-4c0-5-4-7-8-7"/></svg></div>
<div class="abs focus-icon" style="left:944px;top:1179px"><svg width="54" height="50" viewBox="0 0 54 50" fill="none" stroke="#fff" stroke-width="2" stroke-linejoin="round"><circle cx="17" cy="12" r="7"/><circle cx="37" cy="12" r="7"/><path d="M5 46V30c0-6 5-10 12-10M49 46V30c0-6-5-10-12-10M13 46V34M41 46V34M20 30l7-5 7 5-7 6z"/></svg></div>

<svg class="abs" style="left:0;top:1270px" width="1200" height="40" fill="none" stroke="#efb3ad" stroke-width="2.5" stroke-linecap="round">
  <path d="M262 16q22 -8 66 -6M320 4l8 6-9 5"/><path d="M418 16q22 -8 66 -6M476 4l8 6-9 5"/><path d="M566 16q22 -8 66 -6M624 4l8 6-9 5"/><path d="M716 16q22 -8 66 -6M774 4l8 6-9 5"/><path d="M874 16q22 -8 66 -6M932 4l8 6-9 5"/>
</svg>
<div class="abs focus-label" style="left:142px;top:1313px">Aufklären</div>
<div class="abs focus-label" style="left:295px;top:1313px">Erkennen</div>
<div class="abs focus-label" style="left:445px;top:1313px">Benennen</div>
<div class="abs focus-label" style="left:591px;top:1313px">Handeln</div>
<div class="abs focus-label" style="left:745px;top:1313px">Vermitteln</div>
<div class="abs focus-label" style="left:913px;top:1313px">Rückfallprävention</div>

<div class="abs photo-ring" style="left:173px;top:1473px;width:326px;height:326px"></div>
<div class="abs photo" role="img" aria-label="Illustration: Kopf im Profil mit verknäultem Gedankenfaden" style="left:192px;top:1492px;width:288px;height:288px;background:linear-gradient(120deg,#7fbfa9 0%,#6fb39c 45%,#e8d7b8 60%,#d9c6a4 100%)"></div>
<h2 class="abs heading" style="left:543px;top:1531px">Das Trauma</h2>
<div class="abs heading-bar" style="left:543px;top:1569px"></div>
<p class="abs copy" style="left:543px;top:1599px;width:480px;letter-spacing:-0.15px">„Psychologisches, psychisches, seelisches oder mentales Trauma oder Psychotrauma (griech.: Wunde, Pl.: Traumata, Träume) = Erinnerung einer Person an die Situation eines für sie seelisch einschneidenden Erlebnisses bzw. der seelische und/oder neuerdings auch der körperliche (z. B. auf Hirnstrukturen) Eindruck, den das Erlebnis in der Seele der betroffenen Person hinterlassen hat.“ 92</p>
<div class="abs btn" style="left:543px;top:1752px;width:132px">Mehr erfahren</div>

<h2 class="abs heading" style="left:174px;top:1875px">Die Hörschädigung</h2>
<div class="abs heading-bar" style="left:174px;top:1913px"></div>
<p class="abs copy" style="left:174px;top:1942px;width:480px;letter-spacing:-0.15px">Lorem ipsum dolor sit amet, consetetur sadipscing elitr, sed diam nonumy eirmod tempor invidunt ut labore et dolore magna aliquyam erat, sed diam voluptua. At vero eos et accusam et justo duo dolores et ea rebum. Stet clita kasd gubergren, no sea takimata sanctus est Lorem ipsum dolor sit amet.</p>
<div class="abs btn" style="left:174px;top:2082px;width:132px">Mehr erfahren</div>
<div class="abs photo-ring" style="left:701px;top:1829px;width:326px;height:326px"></div>
<div class="abs photo" role="img" aria-label="Foto: Kind mit Kopfhörern vor herbstlichem Laub" style="left:720px;top:1848px;width:288px;height:288px;background:linear-gradient(160deg,#e3c04f 0%,#d9b545 40%,#8ea0b4 75%,#6d8f5c 100%)"></div>
<div class="abs deco" role="img" aria-label="Aquarellfleck" style="left:0;top:2130px;width:190px;height:110px;background:radial-gradient(ellipse,#f3dcdb 0%,rgba(255,255,255,0) 70%)"></div>

<section class="abs band-pink" style="top:2235px;height:635px;background:var(--blush)"></section>
<h2 class="abs heading" style="left:174px;top:2299px">Aktuelles</h2>
<div class="abs heading-bar" style="left:174px;top:2337px"></div>
<p class="abs copy" style="left:174px;top:2366px">Zurück in das Ich finden mit Unterstützung der Netzwerkpartner bzw. Traumaverbund Mittelsachsen</p>

<article class="abs news-card" style="left:174px;top:2433px">
  <div class="news-img" role="img" aria-label="Foto: junge Frau im Freien" style="background:linear-gradient(135deg,#d8b39b,#a8b9c0)"></div>
  <h3 class="news-title">Lorem ipsum dolor sit amet, consetetur sadipscing elitr,</h3>
  <p class="news-text">Lorem ipsum dolor sit amet, consetetur sadipscing elitr, sed diam nonumy eirmod tempor invidunt ut labore et dolore magna aliquyam erat, sed diam voluptua.</p>
  <div class="btn">Weiterlesen</div>
</article>
<article class="abs news-card" style="left:476px;top:2433px">
  <div class="news-img" role="img" aria-label="Foto: Ärztin und Patientin bei einer Untersuchung" style="background:linear-gradient(135deg,#cfcfd2,#efe9e6)"></div>
  <h3 class="news-title">Lorem ipsum dolor sit amet, consetetur sadipscing elitr,</h3>
  <p class="news-text">Lorem ipsum dolor sit amet, consetetur sadipscing elitr, sed diam nonumy eirmod tempor invidunt ut labore et dolore magna aliquyam erat, sed diam voluptua.</p>
  <div class="btn">Weiterlesen</div>
</article>
<article class="abs news-card" style="left:778px;top:2433px">
  <div class="news-img" role="img" aria-label="Foto: zwei Frauen im Gespräch auf einem Sofa" style="background:linear-gradient(135deg,#b7a596,#d9d2c9)"></div>
  <h3 class="news-title">Lorem ipsum dolor sit amet, consetetur sadipscing elitr,</h3>
  <p class="news-text">Lorem ipsum dolor sit amet, consetetur sadipscing elitr, sed diam nonumy eirmod tempor invidunt ut labore et dolore magna aliquyam erat, sed diam voluptua.</p>
  <div class="btn">Weiterlesen</div>
</article>
<div class="abs deco" role="img" aria-label="Aquarellfleck" style="left:850px;top:2700px;width:350px;height:300px;background:radial-gradient(ellipse,rgba(240,218,218,.7) 0%,rgba(255,255,255,0) 70%)"></div>

<h2 class="abs heading" style="left:174px;top:2947px">Kontakt</h2>
<div class="abs heading-bar" style="left:174px;top:2985px"></div>
<div class="abs field" style="left:174px;top:3050px;width:421px;height:50px">Vorname</div>
<div class="abs field" style="left:605px;top:3050px;width:421px;height:50px">Name*</div>
<div class="abs field" style="left:174px;top:3115px;width:852px;height:50px">E-Mailadresse*</div>
<div class="abs field" style="left:174px;top:3181px;width:852px;height:209px">Ihre persönliche Nachricht an Uns...</div>
<div class="abs check" style="left:174px;top:3420px"></div>
<p class="abs" style="left:204px;top:3418px;width:800px;font-size:13px;line-height:20px;color:var(--muted)">Ich habe die Datenschutzerklärung gelesen und stimme zu, dass meine zur Kontaktaufnahme und für Rückfragen übermittelten Angaben gemäß dieser Datenschutzerklärung verwendet werden.*</p>
<div class="abs btn" style="left:174px;top:3484px;width:175px;height:42px;border-radius:21px;gap:10px"><svg width="8" height="12" viewBox="0 0 8 12" fill="none" stroke="#fff" stroke-width="1.8"><path d="M1 1l5 5-5 5"/></svg>Nachricht senden</div>

<footer class="abs site-footer">
  <div class="abs foot-col" style="left:108px">
    <svg width="30" height="36" viewBox="0 0 30 36" fill="none" stroke="#fff" stroke-width="1.6"><path d="M15 34s12-12 12-21a12 12 0 0 0-24 0c0 9 12 21 12 21z"/><circle cx="15" cy="13" r="4.5"/></svg>
    <div>Stadtbund Hörbehinderter<br>Chemnitz e.V.<br>Lindenweg 14<br>09113 Chemnitz</div>
  </div>
  <div class="abs foot-div" style="left:424px"></div>
  <div class="abs foot-col" style="left:482px">
    <svg width="38" height="32" viewBox="0 0 38 32" fill="none" stroke="#fff" stroke-width="1.6"><rect x="1" y="1" width="24" height="17" rx="1"/><path d="M8 18v7l6-7M29 9h8v15h-4v5l-5-5h-9v-6"/></svg>
    <div>Tel.:&nbsp; 0371 40 22 18<br>Mobil: 0160 55 31 472<br>Fax:&nbsp; 0371 40 22 19</div>
  </div>
  <div class="abs foot-div" style="left:746px"></div>
  <div class="abs foot-col" style="left:794px">
    <svg width="42" height="36" viewBox="0 0 42 36" fill="none" stroke="#fff" stroke-width="1.6"><circle cx="11" cy="9" r="6"/><rect x="1" y="20" width="19" height="14"/><circle cx="31" cy="14" r="5"/><rect x="22" y="24" width="18" height="10"/></svg>
    <div>www.ungesehene-schwestern.de<br>kontakt@ungesehene-schwestern.de</div>
  </div>
</footer>
<div class="abs to-top"><svg width="14" height="9" viewBox="0 0 14 9" fill="none" stroke="#a13d6e" stroke-width="1.8"><path d="M1 8l6-6 6 6"/></svg>zurück</div>
<div class="abs legal">
  <div class="abs" style="left:88px;top:22px;display:flex;gap:38px"><a>Impressum</a><a>Datenschutz</a><a>Karriere</a><a>Sitemap</a></div>
  <div class="abs" style="right:89px;top:22px">© 2024 Stadtbund Hörbehinderter Chemnitz e.V.</div>
</div>

</body>
</html>
```